I need some Graphic Design for Planning Poker Cards (AI, PSD, EPS, PDF, PNG)

Hi Designers,

======= PLEASE SEE THE ATTACHMENTS ALSO ========

I would like to design the graphics for Planning Poker cards which are used for Planning Estimation in SCRUM.
You can easily find how the real cards look like by searching it in Google.

I would like to receive the final handover files in these formats: AI, EPS, PSD, PDF, PNG. (Is it Corel Draw format possible?)
And also I want all the Font files which were used in the design.

PLEASE SEE THE ATTACHMENTS FOR:
- Details Requirements - including many samples inside
- Example I found in the internet
- Designed files for Logo of my company (HLNARO)

Thanks,
Khanh.

```html
<!DOCTYPE html>
<html lang="en">
<head>
<meta charset="utf-8">
<title>HLNARO Planning Poker Cards</title>
<link rel="stylesheet" href="https://fonts.googleapis.com/css2?family=Nunito:wght@700;800;900&display=swap">
<style>
  :root {
    --page: #ffffff;
    --navy: #16142b;
    --orange: #e8874f;
    --sand: #f3c98c;
    --rust: #b0503a;
    --cream: #efe6d8;
    --peach: #eea77a;
    --ink-light: #fbf3e8;
  }
  html, body {
    margin: 0;
    padding: 0;
    overflow: hidden;
    background: var(--page);
  }
  .canvas {
    position: relative;
    width: 1200px;
    height: 675px;
    overflow: hidden;
    background: var(--page);
    font-family: "Nunito", sans-serif;
  }
  .card {
    position: absolute;
    top: 175px;
    width: 190px;
    height: 264px;
    border-radius: 8px;
    overflow: hidden;
  }
  .card svg { display: block; width: 100%; height: 100%; }
  .card-back { left: 47px; }
  .card-zero { left: 272px; }
  .card-question { left: 497px; }
  .card-coffee { left: 724px; }
  .card-infinity { left: 947px; }

  .bg-navy { fill: var(--navy); }
  .bg-orange { fill: var(--orange); }
  .bg-sand { fill: var(--sand); }
  .bg-rust { fill: var(--rust); }
  .bg-cream { fill: var(--cream); }
  .bg-peach { fill: var(--peach); }
  .medallion { fill: var(--cream); }
  .medallion-inner { fill: var(--orange); }
  .value-center { fill: var(--cream); font-weight: 900; font-family: "Nunito", sans-serif; }
  .value-corner { fill: var(--ink-light); font-weight: 800; font-family: "Nunito", sans-serif; }
  .brand-center { fill: var(--rust); font-weight: 900; font-family: "Nunito", sans-serif; }
  .brand-foot { fill: var(--navy); font-weight: 900; font-family: "Nunito", sans-serif; }
  .brand-tagline { fill: var(--navy); font-weight: 700; font-family: "Nunito", sans-serif; }
  .brand-dot { fill: none; stroke: var(--rust); stroke-width: 1.6; }
</style>
</head>
<body>
<main class="canvas">

  <div class="card card-back">
    <svg viewBox="0 0 143 198" aria-label="Card back">
      <rect class="bg-navy" width="143" height="198"/>
      <polygon class="bg-rust" points="0,40 60,10 143,40 143,55 0,55"/>
      <polygon class="bg-sand" points="0,30 70,0 100,0 20,55 0,55"/>
      <polygon class="bg-peach" points="0,45 143,25 143,55 0,55"/>
      <rect class="bg-cream" x="0" y="55" width="143" height="78"/>
      <polygon class="bg-rust" points="0,133 143,133 143,142 0,150"/>
      <polygon class="bg-peach" points="0,140 143,145 143,198 0,198"/>
      <polygon class="bg-sand" points="0,160 110,198 0,198"/>
      <polygon class="bg-orange" points="40,150 143,170 143,198 60,198"/>
      <circle class="brand-dot" cx="71.5" cy="84" r="9"/>
      <text class="brand-center" x="71.5" y="110" font-size="11" text-anchor="middle">HLNARO</text>
      <text class="brand-foot" x="71.5" y="185" font-size="13" text-anchor="middle">hlnaro</text>
      <text class="brand-tagline" x="71.5" y="192" font-size="3" text-anchor="middle">ESTIMATE WITH YOUR TEAM</text>
    </svg>
  </div>

  <div class="card card-zero">
    <svg viewBox="0 0 143 198" aria-label="Card zero">
      <rect class="bg-navy" width="143" height="198"/>
      <polygon class="bg-sand" points="68,0 143,0 143,198 0,198 0,105"/>
      <polygon class="bg-orange" points="82,0 143,0 143,198 0,198 0,125"/>
      <polygon class="bg-rust" points="143,80 143,92 58,198 48,198"/>
      <polygon class="bg-navy" points="143,90 143,198 58,198"/>
      <circle class="medallion" cx="71.5" cy="99" r="37" role="img" aria-label="Laurel wreath medallion"/>
      <circle class="medallion-inner" cx="71.5" cy="99" r="25"/>
      <text class="value-center" x="71.5" y="112" font-size="38" text-anchor="middle">0</text>
      <text class="value-corner" x="4" y="16" font-size="15">0</text>
      <text class="value-corner" x="139" y="193" font-size="15" text-anchor="end">0</text>
    </svg>
  </div>

  <div class="card card-question">
    <svg viewBox="0 0 143 198" aria-label="Card question mark">
      <rect class="bg-navy" width="143" height="198"/>
      <polygon class="bg-sand" points="68,0 143,0 143,198 0,198 0,105"/>
      <polygon class="bg-orange" points="82,0 143,0 143,198 0,198 0,125"/>
      <polygon class="bg-rust" points="143,80 143,92 58,198 48,198"/>
      <polygon class="bg-navy" points="143,90 143,198 58,198"/>
      <circle class="medallion" cx="71.5" cy="99" r="37" role="img" aria-label="Laurel wreath medallion"/>
      <circle class="medallion-inner" cx="71.5" cy="99" r="25"/>
      <text class="value-center" x="71.5" y="112" font-size="38" text-anchor="middle">?</text>
      <text class="value-corner" x="4" y="15" font-size="13">?</text>
      <text class="value-corner" x="139" y="193" font-size="13" text-anchor="end">¿</text>
    </svg>
  </div>

  <div class="card card-coffee">
    <svg viewBox="0 0 143 198" aria-label="Card coffee break">
      <rect class="bg-navy" width="143" height="198"/>
      <polygon class="bg-sand" points="68,0 143,0 143,198 0,198 0,105"/>
      <polygon class="bg-orange" points="82,0 143,0 143,198 0,198 0,125"/>
      <polygon class="bg-rust" points="143,80 143,92 58,198 48,198"/>
      <polygon class="bg-navy" points="143,90 143,198 58,198"/>
      <circle class="medallion" cx="71.5" cy="99" r="37" role="img" aria-label="Laurel wreath medallion with coffee cup illustration"/>
      <circle class="medallion-inner" cx="71.5" cy="99" r="25" role="img" aria-label="Coffee cup illustration"/>
      <rect class="bg-cream" x="3" y="3" width="13" height="13" rx="2" role="img" aria-label="Small coffee cup icon"/>
      <rect class="bg-cream" x="127" y="182" width="13" height="13" rx="2" role="img" aria-label="Small coffee cup icon"/>
    </svg>
  </div>

  <div class="card card-infinity">
    <svg viewBox="0 0 143 198" aria-label="Card infinity">
      <rect class="bg-navy" width="143" height="198"/>
      <polygon class="bg-sand" points="68,0 143,0 143,198 0,198 0,105"/>
      <polygon class="bg-orange" points="82,0 143,0 143,198 0,198 0,125"/>
      <polygon class="bg-rust" points="143,80 143,92 58,198 48,198"/>
      <polygon class="bg-navy" points="143,90 143,198 58,198"/>
      <circle class="medallion" cx="71.5" cy="99" r="37" role="img" aria-label="Laurel wreath medallion"/>
      <circle class="medallion-inner" cx="71.5" cy="99" r="25"/>
      <text class="value-center" x="71.5" y="111" font-size="36" text-anchor="middle">∞</text>
      <text class="value-corner" x="3" y="15" font-size="16">∞</text>
      <text class="value-corner" x="140" y="192" font-size="16" text-anchor="end">∞</text>
    </svg>
  </div>

</main>
</body>
</html>
```